Innovative Consulting Firm Needs New Business Cards and Stationary

Our Innovative Consulting Firm, Larkfield Consulting, is in need of new business cards and stationary designs. We want two-sided cards that incorporate our logo, which is attached. We are looking for something not too formal, but is professional and slick.

Card should have the following information:
Name (ex. Tom Bradley)
Title (ex. Manager)
Address (ex. 24680 Cedar Lane)
Address 2 (ex. Suite 100)
City
State
Zip Code
Mobile
Email

The card should also have our website: www.larkfieldconsulting.example

Industry/Entity Type

Management Consulting

Contact Information for Business Card

Name (ex. Tom Bradley)
Title (ex. Manager)
Address 2 (ex. Suite 100)
City
State
Zip Code
Mobile
Email

Font styles to use
Sans Serif

Requirements
Must have
• The colors on the card must match the colors in the logo. The exact color codes are attached in a pdf.
Nice to have
• The Company's Tagline is "Clarity for what's Next". This might be nice to incorporate, but not necessary.

```html
<!DOCTYPE html>
<html lang="en">
<head>
<meta charset="utf-8">
<title>Larkfield Consulting – Business Card</title>
<link href="https://fonts.googleapis.com/css2?family=Arimo:wght@400;700&display=swap" rel="stylesheet">
<style>
  :root {
    --stage: #2b2b2b;
    --navy: #2b4f80;
    --blue-top: #3d6ca8;
    --blue-bottom: #2a4d7e;
    --gold: #e0a81a;
    --paper: #f3f3f2;
    --ink: #2f4f7c;
    --muted: #666a70;
    --white: #ffffff;
  }
  html, body {
    margin: 0;
    padding: 0;
    width: 1200px;
    height: 900px;
    overflow: hidden;
    background: var(--stage);
    font-family: "Arimo", Arial, sans-serif;
  }
  p, ul { margin: 0; padding: 0; }
  .canvas {
    position: relative;
    width: 1200px;
    height: 900px;
  }
  .card {
    position: absolute;
    left: 355px;
    width: 487px;
    height: 271px;
    border-radius: 22px;
    overflow: hidden;
  }
  .card-front {
    top: 158px;
    background: linear-gradient(180deg, var(--blue-top), var(--blue-bottom));
  }
  .card-back {
    top: 467px;
    background: var(--paper);
  }

  /* wordmark */
  .wordmark {
    position: absolute;
    display: flex;
    align-items: center;
    gap: 10px;
    font-weight: 700;
    font-size: 30px;
    letter-spacing: 0.5px;
    white-space: nowrap;
  }
  .wordmark-dot {
    width: 16px;
    height: 16px;
    border-radius: 50%;
    background: var(--gold);
    flex: none;
  }
  .card-front .wordmark {
    left: 0;
    right: 0;
    top: 114px;
    justify-content: center;
    color: var(--white);
  }
  .card-back .wordmark {
    left: 40px;
    top: 42px;
    font-size: 27px;
    color: var(--ink);
  }

  .tagline {
    position: absolute;
    left: 0;
    right: 0;
    top: 226px;
    text-align: center;
    color: var(--gold);
    font-weight: 700;
    font-size: 14px;
    letter-spacing: 1.8px;
  }

  /* contact block */
  .person {
    position: absolute;
    left: 38px;
    top: 146px;
    color: var(--ink);
    font-size: 15px;
  }
  .person-name { letter-spacing: 0.5px; }
  .person-title { font-size: 13.5px; margin-left: 8px; }

  .contact {
    position: absolute;
    top: 177px;
    list-style: none;
    color: var(--muted);
    font-size: 13px;
    line-height: 18px;
  }
  .contact-direct { left: 38px; }
  .contact-address { left: 268px; }
  .contact li {
    display: flex;
    align-items: center;
    gap: 8px;
  }
  .contact .no-icon { padding-left: 20px; }
  .contact svg { width: 12px; height: 12px; flex: none; }

  .swoosh {
    position: absolute;
    left: 0;
    top: 0;
    width: 487px;
    height: 271px;
  }
  .website {
    position: absolute;
    right: 21px;
    top: 242px;
    color: var(--white);
    font-size: 13px;
  }
</style>
</head>
<body>
<main class="canvas">

  <section class="card card-front" aria-label="Card front">
    <div class="wordmark"><span class="wordmark-dot"></span>Larkfield Consulting</div>
    <p class="tagline">Clarity for what's Next</p>
  </section>

  <section class="card card-back" aria-label="Card back">
    <svg class="swoosh" viewBox="0 0 487 271" aria-hidden="true">
      <path d="M150 271 Q 320 196 487 220 L 487 228 Q 330 207 172 271 Z" fill="var(--gold)"/>
      <path d="M172 271 Q 330 207 487 228 L 487 271 Z" fill="var(--navy)"/>
    </svg>

    <div class="wordmark"><span class="wordmark-dot"></span>Larkfield Consulting</div>

    <p class="person"><span class="person-name">TOM BRADLEY</span><span class="person-title">Manager</span></p>

    <ul class="contact contact-direct">
      <li>
        <svg viewBox="0 0 24 24" aria-hidden="true"><path d="M6.6 10.8a15.1 15.1 0 0 0 6.6 6.6l2.2-2.2a1 1 0 0 1 1-.25 11.4 11.4 0 0 0 3.6.57 1 1 0 0 1 1 1V20a1 1 0 0 1-1 1A17 17 0 0 1 3 4a1 1 0 0 1 1-1h3.5a1 1 0 0 1 1 1c0 1.250.2 2.450.57 3.570a1 1 0 0 1-.25 1z" fill="none" stroke="var(--gold)" stroke-width="2"/></svg>
        020 555 0142
      </li>
      <li>
        <svg viewBox="0 0 24 24" aria-hidden="true"><rect x="2" y="5" width="20" height="14" fill="none" stroke="var(--gold)" stroke-width="2"/><path d="M2 5l10 8 10-8" fill="none" stroke="var(--gold)" stroke-width="2"/></svg>
        info@larkfieldconsulting.example
      </li>
    </ul>

    <ul class="contact contact-address">
      <li>
        <svg viewBox="0 0 24 24" aria-hidden="true"><path d="M12 22s7-7.5 7-13a7 7 0 0 0-14 0c0 5.5 7 13 7 13z" fill="none" stroke="var(--gold)" stroke-width="2"/><circle cx="12" cy="9" r="2.5" fill="none" stroke="var(--gold)" stroke-width="2"/></svg>
        Meridiaanweg 27
      </li>
      <li class="no-icon">1187 KT Westerveld</li>
    </ul>

    <p class="website">www.larkfieldconsulting.example</p>
  </section>

</main>
</body>
</html>
```